letterhead package
corin maddox agency
Use same font as used in my logo
any fonts
Professional
Corin Maddox Agency
President
5172 Birchley Rd
Harrowmere VT 11619
info@cmvopr.com
www.cmvopr.com
-national and international horse transportation-
Logo File AI version

```html
<!DOCTYPE html>
<html lang="en">
<head>
<meta charset="utf-8">
<title>Corin Maddox Agency – Business Card</title>
<link href="https://fonts.googleapis.com/css2?family=Arimo:wght@400;700&display=swap" rel="stylesheet">
<style>
  :root {
    --backdrop: #e4e4e4;
    --card-black: #0b0b0b;
    --gold: #d9b42a;
    --gold-light: #f2d55a;
    --gold-dark: #a8841a;
    --text-light: #e9e2c4;
  }
  * { margin: 0; padding: 0; box-sizing: border-box; }
  html, body {
    width: 1200px; height: 901px; overflow: hidden;
    background: var(--backdrop);
    font-family: "Arimo", Arial, sans-serif;
  }
  .canvas {
    width: 1200px; height: 901px;
    display: flex; align-items: center; justify-content: center;
  }
  .business-card {
    position: relative;
    width: 1000px; height: 571px;
    background: var(--card-black);
    overflow: hidden;
    box-shadow: 0 14px 40px rgba(0,0,0,0.25);
  }
  .brand {
    position: absolute; left: 60px; top: 150px; width: 380px; height: 230px;
    display: flex; flex-direction: column; align-items: center; justify-content: center; gap: 18px;
    text-align: center;
  }
  .brand-mark {
    width: 44px; height: 44px; border-radius: 50%;
    background: var(--gold); flex: none;
  }
  .brand-name {
    color: var(--gold);
    font-weight: 700; font-size: 32px; letter-spacing: 1px;
    line-height: 1.2;
  }
  .divider {
    position: absolute; left: 470px; top: 70px;
    width: 2px; height: 330px;
    background: var(--gold);
  }
  .contact-block {
    position: absolute; left: 500px; top: 72px;
  }
  .agency-name {
    color: var(--gold-light); font-size: 30px; font-weight: 400;
  }
  .job-title {
    color: var(--gold); font-size: 20px; letter-spacing: 1px; margin-top: 4px;
  }
  .contact-list { list-style: none; margin-top: 42px; }
  .contact-list li {
    display: flex; align-items: center; gap: 14px;
    color: var(--text-light); font-size: 19px; height: 34px;
  }
  .contact-list li.no-icon { padding-left: 32px; }
  .contact-list svg { width: 18px; height: 18px; fill: var(--gold); flex: none; }
  .rule-top {
    position: absolute; left: 0; right: 0; top: 432px; height: 3px;
    background: var(--gold);
  }
  .web-strip {
    position: absolute; left: 0; right: 0; top: 435px; height: 56px;
    background: var(--card-black);
    display: flex; align-items: center; justify-content: center;
    color: var(--gold-light); font-size: 20px; letter-spacing: 4px;
  }
  .gold-band {
    position: absolute; left: 0; right: 0; top: 491px; bottom: 0;
    background: linear-gradient(180deg, var(--gold-light) 0%, var(--gold) 45%, var(--gold-dark) 100%);
  }
</style>
</head>
<body>
<main class="canvas">
  <section class="business-card">
    <div class="brand">
      <span class="brand-mark"></span>
      <span class="brand-name">CORIN MADDOX<br>AGENCY</span>
    </div>

    <div class="divider"></div>

    <div class="contact-block">
      <div class="agency-name">Corin Maddox Agency</div>
      <div class="job-title">PRESIDENT</div>
      <ul class="contact-list">
        <li>
          <svg viewBox="0 0 24 24"><path d="M12 2a7 7 0 0 0-7 7c0 5 7 13 7 13s7-8 7-13a7 7 0 0 0-7-7zm0 9.5A2.5 2.5 0 1 1 12 6.5a2.5 2.5 0 0 1 0 5z"/></svg>
          5172 Birchley Rd
        </li>
        <li class="no-icon">Harrowmere VT 11619</li>
        <li>
          <svg viewBox="0 0 24 24"><path d="M6.6 10.8a15 15 0 0 0 6.6 6.6l2.2-2.2a1 1 0 0 1 1-.25 11.4 11.4 0 0 0 3.6.57 1 1 0 0 1 1 1V20a1 1 0 0 1-1 1A17 17 0 0 1 3 4a1 1 0 0 1 1-1h3.5a1 1 0 0 1 1 1c0 1.25.2 2.45.57 3.57a1 1 0 0 1-.25 1z"/></svg>
          555 301 0142
        </li>
        <li>
          <svg viewBox="0 0 24 24"><path d="M6.6 10.8a15 15 0 0 0 6.6 6.6l2.2-2.2a1 1 0 0 1 1-.25 11.4 11.4 0 0 0 3.6.57 1 1 0 0 1 1 1V20a1 1 0 0 1-1 1A17 17 0 0 1 3 4a1 1 0 0 1 1-1h3.5a1 1 0 0 1 1 1c0 1.25.2 2.450.57 3.57a1 1 0 0 1-.25 1z"/></svg>
          555 301 0187
        </li>
        <li>
          <svg viewBox="0 0 24 24"><path d="M6.6 10.8a15 15 0 0 0 6.6 6.6l2.2-2.2a1 1 0 0 1 1-.25 11.4 11.4 0 0 0 3.6.57 1 1 0 0 1 1 1V20a1 1 0 0 1-1 1A17 17 0 0 1 3 4a1 1 0 0 1 1-1h3.5a1 1 0 0 1 1 1c0 1.25.2 2.45.57 3.57a1 1 0 0 1-.25 1z"/></svg>
          555 301 0163
        </li>
        <li>
          <svg viewBox="0 0 24 24"><path d="M2 5h20v14H2zm2 2v.5l8 5 8-5V7zm0 3v7h16v-7l-8 5z"/></svg>
          info@cmvopr.com
        </li>
      </ul>
    </div>

    <div class="rule-top"></div>
    <div class="web-strip">www.cmvopr.com</div>
    <div class="gold-band"></div>
  </section>
</main>
</body>
</html>
```